依頼詳細
従業員10名以上の企業にマイクロバスレンタカーの利用を促すチラシを配布する事になりました。コロナ終息後に企業の担当者が思わず話を聞いてみたいと思われるチラシの作成をお願い致します。
記載項目
本社:株式会社ミドリヤマ運輸
530-0087
大阪府大阪市北区天満橋5丁目8番2号 桜川フクダビル9階
TEL: 0120-472-915(06-6248-3957) FAX: 06-6248-3951
Mail:info@kazemidori-rent.example.jp
URL:http://www.kazemidori-rent.example.jp

東京支店
東京都千代田区神田須田町4丁目2番7 ルミナス須田ビル3階
TEL:03-5847-2396 FAX:03-5847-2397

サイズ
A4
ページ数
両面
希望イメージ
シンプル 複雑
単色 カラフル
暗い 明るい
日常 高級
遊び心 厳粛
未来的 伝統的
女性的 男性的
希望する色
青系、茶系、無彩色系
納品ファイル
• イラストレーター形式 (.ai)
• フォトショップ形式 (.psd)
補足説明
前回親会社が作成したチラシがありましたので参考までにお送りさせて頂きます。
株式会社ミドリヤマ運輸ロゴです。
チラチ表面・裏面で必ず入れて入れたい情報(改)
会社のロゴやチラシ作成で記載をお願いしたい情報を纏めさせて頂きました。
チラシ作成にあたり、記載をして欲しい事を纏めております。
住所ラベル
【60×105mm】のスペース必須でデザインをよろしくお願い申し上げます。
高級感を醸し出す作品の提供を宜しくお願い致します
弊社は高年式のマイクロバスを多数所有しております。
装備内容も標準装備でこれだけ付いている会社はないと自負しております。
写真追加させていただきます
安全•安心•快適にお過ごし頂く為にドライバーも含めたトータルサポートを
是非この機会にご検討くださいませ。
※違反行為をしている会社と判断をされ、イメージが悪くなる為

マイクロバスは送迎はもちろん、日帰りや1泊2日の観光旅行などにもよく利用されております。
ある種絞り込みをした文面がインパクトある為、送迎に関する事のみ記載

※上記文面に対して社内より問題ありと判断された為、削除をお願い出来ないでしょうか?
お手数お掛け致しますが何卒宜しくお願い致します。
■ 選んだ理由

入選された皆様

いつも大変お世話になっております。
株式会社ミドリヤマ運輸の森下敏彦です。
この度はチラシ作成に尽力頂きありがとうございます。
見やすさ、高級感なおかつレンタカーのイメージがわかりやすいモノを選ばせて頂きました。
最後になりますが入選された作品のai データの送付を宜しくお願い致します。
この度は本当にお疲れ様でした。

■ 提案者全員のお礼・コメント

いつも大変お世話になっております。この度は本当に弊社チラシ作成に尽力を頂きありがとうございます。これからも皆様のお力をお借りすると思いますので引き続き宜しくお願い致します。

```html
<!DOCTYPE html>
<html lang="ja">
<head>
<meta charset="utf-8">
<title>マイクロバス専門のレンタカー会社 チラシ</title>
<link rel="stylesheet" href="https://fonts.googleapis.com/css2?family=Noto+Sans+JP:wght@400;500;700&family=Noto+Serif+JP:wght@600;700;900&display=swap">
<style>
:root{
  --navy:#1d2a52;
  --navy-deep:#141d3d;
  --blue:#2f5fa8;
  --sky:#d9e4f1;
  --grey:#9a9a9a;
  --ink:#2b2b2b;
  --paper:#ffffff;
}
*{box-sizing:border-box;margin:0;padding:0}
html,body{width:849px;height:1200px;overflow:hidden;background:var(--paper)}
.flyer{position:relative;width:849px;height:1200px;overflow:hidden;background:var(--paper);font-family:"Noto Sans JP",sans-serif;color:var(--ink)}
.band{position:absolute;inset:0;width:849px;height:1200px}
.label-space{position:absolute;left:34px;top:26px;width:258px;height:148px;border:1.5px dashed var(--grey);background:#f4f4f4;color:var(--grey);font-size:13px;padding:14px 18px;line-height:1.5}
.contact-name{position:absolute;left:338px;top:26px;width:130px;border-bottom:1px solid var(--grey);font-size:11px;color:var(--grey);padding-bottom:4px}
.brand{position:absolute;right:30px;top:28px;display:flex;align-items:center;gap:8px;color:var(--navy);font-weight:700;font-size:15px;line-height:1.1;text-align:right}
.brand-sub{font-size:10px}
.brand-mark{width:14px;height:14px;border-radius:50%;background:var(--navy)}
.intro{position:absolute;left:338px;top:80px;width:250px;font-size:13.5px;line-height:1.75;color:var(--ink)}
.use-list{position:absolute;left:28px;top:318px;list-style:none;font-size:15px;font-weight:700;color:var(--navy);line-height:1.62}
.features{position:absolute;left:440px;top:300px;width:178px;background:var(--paper);border:1px solid var(--sky);padding:10px 10px 12px;text-align:center;color:var(--navy)}
.features-note{font-size:10.5px;line-height:1.4;border-bottom:1px solid var(--sky);padding-bottom:6px;margin-bottom:6px}
.features-items{font-size:14px;font-weight:700;line-height:1.45}
.features-tag{display:inline-block;margin-top:4px;background:var(--navy);color:var(--paper);font-size:12px;padding:2px 10px}
.bus-photo{position:absolute;left:0;top:520px;width:540px;height:200px;background:linear-gradient(180deg,#c9d6e6 0%,#e9eef3 45%,#8f98a3 80%,#5d636b 100%)}
.caption{position:absolute;left:28px;top:662px;font-size:13px;font-weight:700;color:var(--paper);line-height:1.5;text-shadow:0 0 3px rgba(0,0,0,.5)}
.headline{position:absolute;writing-mode:vertical-rl;font-family:"Noto Serif JP",serif;font-weight:900;color:var(--paper);line-height:1;letter-spacing:.04em}
.headline-a{left:762px;top:420px;font-size:58px}
.headline-b{left:668px;top:420px;font-size:58px}
.headline-b small{font-size:32px}
.sub{position:absolute;writing-mode:vertical-rl;font-family:"Noto Serif JP",serif;font-weight:600;color:var(--paper);font-size:29px;letter-spacing:.08em;line-height:1}
.sub-1{left:606px;top:465px}
.sub-2{left:558px;top:620px}
.sub-3{left:510px;top:790px}
.info{position:absolute;left:28px;top:740px;width:440px}
.info-block{margin-bottom:14px}
.info-title{font-size:14px;font-weight:700;color:var(--blue);border-bottom:1px solid var(--blue);padding-bottom:3px;margin-bottom:5px}
.info-text{font-size:11px;line-height:1.6}
.checks{display:flex;gap:14px;font-size:11px;margin-top:2px}
</style>
</head>
<body>
<div class="flyer">
  <svg class="band" viewBox="0 0 849 1200" aria-hidden="true">
    <polygon points="640,280 849,150 849,1200 470,1200 470,380" fill="var(--navy)"/>
    <polygon points="849,150 849,190 640,318 640,280" fill="var(--blue)"/>
    <polygon points="470,1200 440,1200 440,400 470,380" fill="var(--sky)"/>
  </svg>

  <div class="label-space">宛名ラベル<br>60×105mm</div>
  <div class="contact-name">担当者名</div>
  <div class="brand"><span>MIDORIYAMA<br><span class="brand-sub">Rent A Car</span></span><span class="brand-mark"></span></div>

  <p class="intro">レンタカー送迎を導入または検討されている皆様、コスト削減と業務化を図るご提案をさせて頂きます。</p>

  <ul class="use-list">
    <li>店頭視察、工場見学、物件見学の送迎</li>
    <li>企業や学校の研修移動</li>
    <li>ゴルフコンペの送迎</li>
    <li>通夜・告別式</li>
    <li>遠征試合・合宿</li>
    <li>イベント送迎</li>
    <li>機材ロケバス など</li>
  </ul>

  <div class="features">
    <p class="features-note">車両はすべて<br>高年式モデル新車種</p>
    <p class="features-items">ETC　ナビ<br>バックモニター<br>ドライブレコーダー</p>
    <span class="features-tag">全て標準装備</span>
  </div>

  <div class="bus-photo" role="img" aria-label="並んで駐車している白いマイクロバスの写真"></div>
  <p class="caption">マイクロバスは<br>様々な送迎に対応します。</p>

  <h1 class="headline headline-a">マイクロバス専門の</h1>
  <h1 class="headline headline-b">レンタカー会社<small>だからこそ</small></h1>
  <p class="sub sub-1">マイクロバスに関する</p>
  <p class="sub sub-2">様々な問題と課題を</p>
  <p class="sub sub-3">解決致します。</p>

  <div class="info">
    <section class="info-block">
      <h2 class="info-title">送迎バスの運行管理会社のご紹介</h2>
      <p class="info-text">自家用自動車管理業と提携し運行管理の負担を軽減致します。<br>経験豊富なドライバーの手配まで一括でサポート致します。</p>
    </section>
    <section class="info-block">
      <h2 class="info-title">運行全面を支援</h2>
      <p class="info-text">送迎の導入から日々の運行計画まで丁寧にご相談を承ります。<br>安全・安心・快適な送迎を社内負担なく実現致します。</p>
    </section>
    <section class="info-block">
      <h2 class="info-title">今すぐ送迎バスが必要</h2>
      <p class="info-text">短期のご利用も柔軟に対応し、最短でご用意致します。</p>
      <div class="checks"><span>□スポット利用</span><span>□納車前代車</span><span>□お試し導入</span></div>
    </section>
    <section class="info-block">
      <h2 class="info-title">所有車両を買い取ってほしい</h2>
      <p class="info-text">ご不要になった車両も適正価格にて買い取り致します。<br>入替えと合わせたご提案も可能ですのでお気軽にご相談ください。</p>
    </section>
  </div>
</div>
</body>
</html>
```